New Business Cards for MB&LR

We need updated business cards for a staff of 15 engineers, estimators, project managers, and sales people. We have recently begun changes to our website and marketing material to improve our look and branding. We are an established fabricator specializing in pressure vessels, tanks, and structural steel. The owners require us to use the existing logo and old english text design. Also, we prefer dark grey or mostly black cards.
Target Market(s)
Engineers, purchasing agents, estimators, and project managers of; mining companies, refineries, industrial construction professionals
Industry/Entity Type
Business
Contact Information for Business Card
Logo, phone, website, email, etc.
Look and feel

```html
<!DOCTYPE html>
<html lang="en">
<head>
<meta charset="utf-8">
<title>MB&amp;LR Business Cards</title>
<link rel="stylesheet" href="https://fonts.googleapis.com/css2?family=Playfair+Display:wght@700&family=Roboto:wght@400;500&display=swap">
<style>
  :root {
    --page: #c6c6c6;
    --card: #ffffff;
    --ink: #111111;
    --panel: #0b0b0b;
    --panel-text: #ffffff;
    --muted: #b5b5b5;
    --rule: #ffffff;
  }
  * { box-sizing: border-box; margin: 0; padding: 0; }
  html, body { width: 1200px; height: 1200px; overflow: hidden; }
  body { background: var(--page); position: relative; font-family: "Roboto", sans-serif; }

  .card {
    position: absolute;
    left: 240px;
    width: 720px;
    height: 412px;
    background: var(--card);
    box-shadow: 0 6px 18px rgba(0,0,0,0.18);
    overflow: hidden;
  }
  .card--front { top: 120px; }
  .card--back { top: 660px; }

  /* Wordmark that stands where the mark sits */
  .wordmark {
    position: absolute;
    display: flex;
    align-items: center;
    gap: 12px;
    font-family: "Playfair Display", serif;
    font-weight: 700;
    color: var(--ink);
  }
  .wordmark__square {
    width: 22px; height: 22px;
    border: 3px solid var(--ink);
  }
  .company {
    position: absolute;
    font-family: "Playfair Display", serif;
    font-weight: 700;
    color: var(--ink);
    text-align: center;
  }

  .card--front .wordmark { left: 64px; top: 150px; font-size: 44px; }
  .card--front .company { left: 30px; width: 310px; top: 232px; font-size: 20px; line-height: 1.25; }

  .card--back .wordmark { left: 0; right: 0; justify-content: center; top: 130px; font-size: 64px; }
  .card--back .company { left: 0; width: 100%; top: 258px; font-size: 28px; }

  /* Dark contact panel */
  .panel {
    position: absolute;
    top: 38px;
    right: 0;
    width: 390px;
    height: 336px;
    background: var(--panel);
    clip-path: polygon(22px 0, 100% 0, 100% 100%, 0 100%);
    color: var(--panel-text);
  }
  .panel::before, .panel::after {
    content: "";
    position: absolute;
    left: 0; right: 0;
    height: 3px;
    background: var(--rule);
  }
  .panel::before { top: 10px; }
  .panel::after { bottom: 10px; }
  .panel-shadow {
    position: absolute;
    top: 38px;
    left: 312px;
    width: 40px;
    height: 336px;
    background: linear-gradient(to right, rgba(0,0,0,0), rgba(0,0,0,0.16));
    clip-path: polygon(18px 0, 40px 0, 18px 100%, 0 100%);
  }
  .person { position: absolute; left: 50px; top: 54px; }
  .person__name {
    font-family: "Playfair Display", serif;
    font-weight: 700;
    font-size: 26px;
    letter-spacing: 0.5px;
  }
  .person__role { font-size: 12px; color: var(--muted); margin-top: 6px; }

  .contacts { position: absolute; left: 46px; top: 140px; list-style: none; }
  .contacts li {
    display: flex;
    align-items: flex-start;
    gap: 14px;
    font-size: 13px;
    line-height: 1.3;
    margin-bottom: 13px;
  }
  .contacts__badge {
    flex: none;
    width: 15px; height: 15px;
    border-radius: 50%;
    background: var(--panel-text);
    color: var(--panel);
    font-size: 8px;
    font-weight: 500;
    display: flex; align-items: center; justify-content: center;
    margin-top: 1px;
  }
  .panel__ticks { position: absolute; left: 46px; bottom: 22px; }
</style>
</head>
<body>
  <section class="card card--front" aria-label="Business card front">
    <div class="wordmark"><span class="wordmark__square"></span>MB&amp;LR</div>
    <p class="company">Midvale Boiler &amp;<br>Ledge Rolling</p>
    <div class="panel-shadow"></div>
    <div class="panel">
      <div class="person">
        <h1 class="person__name">DANA WHITLOW</h1>
        <p class="person__role">Managing Director</p>
      </div>
      <ul class="contacts">
        <li><span class="contacts__badge">T</span>801.555.0142</li>
        <li><span class="contacts__badge">F</span>801.555.0187</li>
        <li><span class="contacts__badge">A</span>480 East 200 South,<br>Granite Falls 84190</li>
        <li><span class="contacts__badge">W</span>www.mbandlr.com</li>
      </ul>
      <svg class="panel__ticks" width="10" height="40" viewBox="0 0 10 40">
        <line x1="2" y1="0" x2="2" y2="40" stroke="#555" stroke-width="1"/>
        <line x1="7" y1="0" x2="7" y2="40" stroke="#555" stroke-width="1"/>
      </svg>
    </div>
  </section>

  <section class="card card--back" aria-label="Business card back">
    <div class="wordmark"><span class="wordmark__square"></span>MB&amp;LR</div>
    <p class="company">Midvale Boiler &amp; Ledge Rolling</p>
  </section>
</body>
</html>
```